Business Card

To design a professional business card for myself a Beauty Therapist. I will be selling Sol Varenne tanning and other products from home (a beauty room). I have uploaded a file of there promo and I really love their colours. I'm looking for a classey feel to the design, simple but effective. I require my name Tessa Marlowe Beauty Therapist, Mobile- 0413952817, Email - tessa.marlowe@qelmail.com, Facebook - /tessamarlowebeauty & instagram - tessamarlowebeautytherapist . I would like the logo for facebook and instagram. I will also need a A5 & A4 flyer. text futura book to be used.

```html
<!DOCTYPE html>
<html lang="en">
<head>
<meta charset="utf-8">
<title>Tessa Marlowe – Beauty Therapist Business Card</title>
<link href="https://fonts.googleapis.com/css2?family=Jost:wght@300;400&family=Yellowtail&display=swap" rel="stylesheet">
<style>
  :root {
    --page: #f1efed;
    --mint: #ebf6f5;
    --mint-pattern: #e3f1f0;
    --teal: #66c7c7;
    --teal-deep: #5ab9b9;
    --teal-pattern: #72cccc;
    --white: #ffffff;
    --icon-dark: #3e8f8f;
  }
  * { box-sizing: border-box; margin: 0; padding: 0; }
  html, body {
    width: 1047px;
    height: 1200px;
    overflow: hidden;
    background: var(--page);
  }
  .sheet {
    position: relative;
    width: 1047px;
    height: 1200px;
  }

  /* Front face */
  .card-front {
    position: absolute;
    left: 0; top: 0;
    width: 1047px;
    height: 597px;
    overflow: hidden;
    background: var(--mint);
  }
  .card-front .pattern-fill {
    position: absolute;
    inset: 0;
    background: radial-gradient(ellipse at 50% 40%, var(--mint) 0%, var(--mint-pattern) 100%);
  }
  .name-first,
  .name-last {
    position: absolute;
    font-family: "Yellowtail", cursive;
    color: var(--teal);
    white-space: nowrap;
    line-height: 1;
    transform-origin: left bottom;
  }
  .name-first {
    left: 4px;
    top: 70px;
    font-size: 390px;
    transform: rotate(-12deg);
    letter-spacing: -6px;
  }
  .name-last {
    left: 268px;
    top: 350px;
    font-size: 150px;
    transform: rotate(-19deg);
  }
  .job-title {
    position: absolute;
    left: 704px;
    top: 522px;
    font-family: "Jost", sans-serif;
    font-weight: 300;
    font-size: 28px;
    letter-spacing: 0.5px;
    color: var(--teal);
  }

  /* Back face */
  .card-back {
    position: absolute;
    left: 21px;
    top: 624px;
    width: 1005px;
    height: 555px;
    overflow: hidden;
    background: var(--teal);
  }
  .card-back .pattern-fill {
    position: absolute;
    inset: 0;
    background: radial-gradient(ellipse at 50% 50%, var(--teal-pattern) 0%, var(--teal) 100%);
  }
  .contact-list {
    position: absolute;
    left: 0;
    right: 0;
    top: 186px;
    list-style: none;
    display: flex;
    flex-direction: column;
    align-items: center;
    gap: 12px;
    font-family: "Jost", sans-serif;
    font-weight: 300;
    font-size: 32px;
    color: var(--white);
  }
  .contact-item {
    display: flex;
    align-items: center;
    gap: 8px;
    height: 38px;
    text-transform: uppercase;
  }
  .contact-item svg { display: block; flex: none; }
  .social-square {
    width: 28px;
    height: 28px;
    background: var(--icon-dark);
    flex: none;
  }
</style>
</head>
<body>
<main class="sheet">
  <section class="card-front">
    <div class="pattern-fill" role="img" aria-label="Faint damask swirl pattern in pale mint"></div>
    <div class="name-first">Tessa</div>
    <div class="name-last">Marlowe</div>
    <p class="job-title">BEAUTY THERAPIST</p>
  </section>

  <section class="card-back">
    <div class="pattern-fill" role="img" aria-label="Tone-on-tone damask swirl pattern in teal"></div>
    <ul class="contact-list">
      <li class="contact-item contact-phone">
        <svg width="22" height="32" viewBox="0 0 22 32" aria-hidden="true">
          <path d="M8 1 C3 3 1 9 2 16 C3 23 7 29 12 31 L15 30 L12 22 L9 23 C7 19 7 13 8 9 L11 9 L12 1 Z" fill="var(--icon-dark)"/>
        </svg>
        <span>0413952817</span>
      </li>
      <li class="contact-item contact-email">
        <svg width="42" height="28" viewBox="0 0 42 28" aria-hidden="true">
          <rect x="1.5" y="1.5" width="39" height="25" fill="none" stroke="var(--icon-dark)" stroke-width="2"/>
          <path d="M1.5 1.5 L21 16 L40.5 1.5 M1.5 26.5 L16 12 M40.5 26.5 L26 12" fill="none" stroke="var(--icon-dark)" stroke-width="2"/>
        </svg>
        <span>tessa.marlowe@qelmail.com</span>
      </li>
      <li class="contact-item contact-social">
        <span class="social-square" aria-hidden="true"></span>
        <span>tessamarlowebeauty</span>
      </li>
      <li class="contact-item contact-social">
        <span class="social-square" aria-hidden="true"></span>
      </li>
    </ul>
  </section>
</main>
</body>
</html>
```